Creative & Professional Business Card for hair salon

We are looking to update our business cards. Our salon is creative, modern, progressive and professional and looking for a design that will reflect this.

```html
<!DOCTYPE html>
<html lang="en">
<head>
<meta charset="utf-8">
<title>Silver Mist Studio – Business Card</title>
<link href="https://fonts.googleapis.com/css2?family=Lato:wght@300;400;700&display=swap" rel="stylesheet">
<style>
  :root {
    --page-bg: #e9ebec;
    --card-bg: #ffffff;
    --brand-blue: #3f6d8c;
    --brand-teal: #6f9fb2;
    --band-dark: #44728f;
    --band-light: #7ba8b9;
    --text-dark: #2f3336;
    --rule: #cfd3d6;
    --ghost: #eef2f4;
  }
  html, body {
    margin: 0;
    width: 1200px;
    height: 844px;
    overflow: hidden;
    background: var(--page-bg);
    font-family: "Lato", sans-serif;
  }
  .stage {
    position: relative;
    width: 1200px;
    height: 844px;
  }
  .card {
    position: absolute;
    top: 270px;
    width: 520px;
    height: 297px;
    background: var(--card-bg);
    box-shadow: 0 6px 18px rgba(0,0,0,0.14);
    overflow: hidden;
  }
  .card--front { left: 50px; }
  .card--back { left: 630px; }

  /* Front */
  .brand {
    position: absolute;
    top: 34px;
    right: 34px;
    display: flex;
    align-items: center;
    gap: 10px;
    color: var(--brand-teal);
    font-weight: 300;
    font-size: 25px;
    letter-spacing: 0.3px;
  }
  .brand__dot {
    width: 14px;
    height: 14px;
    border-radius: 50%;
    background: var(--brand-teal);
  }
  .brand-sub {
    position: absolute;
    top: 70px;
    right: 36px;
    color: var(--brand-teal);
    font-weight: 300;
    font-size: 12px;
    letter-spacing: 0.5px;
  }
  .rule {
    position: absolute;
    left: 30px;
    right: 30px;
    height: 1px;
    background: var(--rule);
  }
  .rule--1 { top: 104px; }
  .rule--2 { top: 124px; }
  .rule--3 { top: 186px; }
  .rule--4 { top: 226px; }
  .person {
    position: absolute;
    left: 30px;
    top: 136px;
  }
  .person__name {
    margin: 0;
    color: var(--brand-blue);
    font-weight: 700;
    font-size: 20px;
    letter-spacing: 0.4px;
    text-transform: uppercase;
  }
  .person__role {
    margin: 1px 0 0;
    color: var(--text-dark);
    font-size: 14px;
  }
  .address {
    position: absolute;
    left: 30px;
    top: 197px;
    margin: 0;
    color: var(--text-dark);
    font-size: 14px;
  }
  .contact {
    position: absolute;
    left: 30px;
    top: 239px;
    margin: 0;
    color: var(--text-dark);
    font-size: 14px;
    white-space: nowrap;
  }
  .contact__label { color: var(--brand-blue); font-weight: 700; }
  .contact__web { color: var(--brand-blue); }

  /* Back */
  .ghost-name {
    position: absolute;
    left: 22px;
    top: 34px;
    color: var(--ghost);
    font-weight: 300;
    font-size: 44px;
    letter-spacing: 1px;
  }
  .write-line {
    position: absolute;
    left: 230px;
    right: 30px;
    height: 1px;
    background: var(--rule);
  }
  .write-line--1 { top: 48px; }
  .write-line--2 { top: 102px; }
  .write-line--3 { top: 156px; }
  .band {
    position: absolute;
    left: 0;
    right: 0;
    bottom: 0;
    height: 110px;
    background: linear-gradient(90deg, var(--band-dark), var(--band-light));
  }
  .social {
    position: absolute;
    top: 14px;
    left: 0;
    right: 0;
    display: flex;
    flex-direction: column;
    align-items: center;
    gap: 6px;
    color: #ffffff;
    font-size: 14px;
  }
  .social__dot {
    width: 20px;
    height: 20px;
    border-radius: 50%;
    background: #ffffff;
  }
</style>
</head>
<body>
<main class="stage">
  <section class="card card--front" aria-label="Business card front">
    <div class="brand"><span class="brand__dot"></span>Silver Mist Studio</div>
    <div class="brand-sub">by Lena Marsh</div>
    <div class="rule rule--1"></div>
    <div class="rule rule--2"></div>
    <div class="person">
      <h1 class="person__name">Daniel Harper</h1>
      <p class="person__role">Managing Director</p>
    </div>
    <div class="rule rule--3"></div>
    <p class="address">17 Linden Row, 30418 Northvale</p>
    <div class="rule rule--4"></div>
    <p class="contact">
      <span class="contact__label">P:</span> 021-555 0148 |
      <span class="contact__label">E:</span> hello@silvermist.example |
      <span class="contact__web">www.silvermiststudio.example</span>
    </p>
  </section>

  <section class="card card--back" aria-label="Business card back">
    <div class="ghost-name">Silver Mist</div>
    <div class="write-line write-line--1"></div>
    <div class="write-line write-line--2"></div>
    <div class="write-line write-line--3"></div>
    <div class="band">
      <div class="social">
        <span class="social__dot"></span>
        <span>www.silvermist-social.example</span>
      </div>
    </div>
  </section>
</main>
</body>
</html>
```